I want a minimal signage design for my pool service company.

Design a premium modern lower-door decal/wrap for a graphite Marrick Dunefield dual cab ute.
The design should look tough, clean and high-end. Think factory/OEM style graphics rather than a typical tradie signwriting setup.
Style:
* Modern and aggressive
* Minimal but eye-catching
* Fluro/electric blue accents
* Suit graphite grey paint
* Motorsport / Velden Kestrel inspired
* Premium marine/pool industry feel
Placement:
* Runs across the lower section of both doors
* Can slightly extend toward rear tray/front guard
* Must flow nicely with the shape of the ute
Include:
* Lakeshore Tide Care logo
* 0491 358 217
Avoid:
* Big rectangular blocks
* Cheap-looking wrap styles
* Too much text
* Overly busy graphics
The design should look professional enough that it could suit a high-end branded company vehicle while still standing out on the road.
Needs to be a ai/pdf/svg file and dimensions will be about 1600mm x 200mm
Pool service

```html
<!DOCTYPE html>
<html lang="en">
<head>
<meta charset="utf-8">
<title>Lakeshore Tide Care – Door Decal Concepts</title>
<link rel="stylesheet" href="https://fonts.googleapis.com/css2?family=Oswald:wght@600&family=Barlow+Condensed:ital,wght@1,600&display=swap">
<style>
  :root{
    --navy:#15123a;
    --blue:#5a93d0;
    --blue-soft:#7fb0e3;
    --white:#ffffff;
    --panel:#bdbdbd;
    --sky:#c9d6e6;
    --water:#8ea5bc;
    --asphalt:#6b6b6d;
    --graphite:#4a4b50;
  }
  *{margin:0;padding:0;box-sizing:border-box}
  html,body{width:1200px;height:2806px;overflow:hidden;background:var(--white)}
  .sheet{position:relative;width:1200px;height:2806px}
  .mockup{position:absolute;left:0;width:1200px;height:900px;
    background:linear-gradient(180deg,var(--sky) 0%,var(--sky) 30%,var(--water) 38%,var(--graphite) 45%,var(--graphite) 58%,var(--asphalt) 62%,var(--asphalt) 100%)}
  .mockup--a{top:0}
  .mockup--b{top:900px}
  .mockup .decal{position:absolute;left:348px;width:380px;height:56px}
  .mockup--a .decal{top:458px}
  .mockup--b .decal{top:1354px;top:454px}
  .artboard{position:absolute;left:0;top:1855px;width:1200px;height:890px;background:var(--panel)}
  .artboard .decal{position:absolute;left:0;width:1160px;height:170px}
  .decal--logo-top{top:205px}
  .decal--logo-low{top:475px}
  .brand-name{font-family:"Oswald",sans-serif;font-weight:600}
  .phone{font-family:"Barlow Condensed",sans-serif;font-weight:600;font-style:italic}
</style>
</head>
<body>
<div class="sheet">

  <svg width="0" height="0" style="position:absolute" aria-hidden="true">
    <defs>
      <symbol id="decal-logo-top" viewBox="0 0 1160 170">
        <path d="M5 3 H530 L570 28 H1110 Q1122 28 1128 40 L1155 90 L1135 120 H690 L676 165 H105 Q92 165 84 152 Z" fill="var(--white)"/>
        <path d="M14 8 H525 L566 33 H1106 Q1116 33 1121 43 L1145 90 L1130 114 H680 L668 158 H108 Q98 158 92 148 Z" fill="var(--blue)"/>
        <path d="M14 8 H62 L168 158 H108 Q98 158 92 148 Z" fill="var(--navy)"/>
        <path d="M92 70 H510 L575 150 L585 158 H182 Z" fill="var(--navy)"/>
        <path d="M118 92 H500 L548 150" fill="none" stroke="var(--white)" stroke-width="4"/>
        <path d="M595 40 H1100 Q1108 40 1112 48 L1134 90 L1122 108 H670 Z" fill="var(--navy)"/>
        <g fill="var(--blue-soft)">
          <rect x="712" y="48" width="110" height="4"/>
        </g>
        <circle cx="162" cy="42" r="12" fill="var(--navy)"/>
        <text class="brand-name" x="188" y="58" font-size="42" fill="var(--navy)">Lakeshore Tide Care</text>
        <text class="phone" x="872" y="102" font-size="76" fill="var(--white)" text-anchor="middle">0491 358 217</text>
      </symbol>

      <symbol id="decal-logo-low" viewBox="0 0 1160 170">
        <path d="M5 20 H140 L152 3 H165 L175 20 H520 L560 42 H1110 Q1122 42 1128 54 L1155 100 L1135 128 H690 L640 165 H105 Q92 165 84 152 Z" fill="var(--white)"/>
        <path d="M14 25 H518 L556 47 H1106 Q1116 47 1121 57 L1145 100 L1130 122 H680 L632 158 H108 Q98 158 92 148 Z" fill="var(--blue)"/>
        <path d="M14 25 H80 L90 110 L70 158 H108 Q98 158 92 148 Z" fill="var(--navy)"/>
        <path d="M80 100 H560 L632 158 H96 Z" fill="var(--navy)"/>
        <path d="M90 112 H548 L600 150" fill="none" stroke="var(--white)" stroke-width="4"/>
        <path d="M595 52 H1100 Q1108 52 1112 60 L1134 100 L1122 116 H670 Z" fill="var(--navy)"/>
        <rect x="735" y="58" width="110" height="4" fill="var(--blue-soft)"/>
        <circle cx="160" cy="60" r="14" fill="var(--navy)"/>
        <text class="brand-name" x="142" y="146" font-size="40" fill="var(--white)">Lakeshore Tide Care</text>
        <text class="phone" x="872" y="112" font-size="76" fill="var(--white)" text-anchor="middle">0491 358 217</text>
      </symbol>
    </defs>
  </svg>

  <section class="mockup mockup--a" role="img" aria-label="Photograph of a graphite dual cab ute parked by a harbour with a steel arch bridge behind, showing the decal on the lower doors">
    <svg class="decal" viewBox="0 0 1160 170" aria-hidden="true"><use href="#decal-logo-top"/></svg>
  </section>

  <section class="mockup mockup--b" role="img" aria-label="Photograph of the same graphite dual cab ute by the harbour, showing the second decal option on the lower doors">
    <svg class="decal" viewBox="0 0 1160 170" aria-hidden="true"><use href="#decal-logo-low"/></svg>
  </section>

  <section class="artboard" aria-label="Flat decal artwork">
    <svg class="decal decal--logo-top" viewBox="0 0 1160 170" role="img" aria-label="Lakeshore Tide Care door decal, 0491 358 217"><use href="#decal-logo-top"/></svg>
    <svg class="decal decal--logo-low" viewBox="0 0 1160 170" role="img" aria-label="Lakeshore Tide Care door decal, alternate layout, 0491 358 217"><use href="#decal-logo-low"/></svg>
  </section>

</div>
</body>
</html>
```